Business card por a urban DJ, up scale audience target

Need a sober design, modern, conservative colors but i can consider some options, y play rnb, hip hop, EDM and top40.

Business card for contact and personal info, double sided, use logo attrached please; im 42 so i need a card acording to my age an target audience.

Target Market(s)

Adult people, up scale audience

Industry/Entity Type

Music Download

Contact Information for Business Card

Cel (318) 5024471963 www.kelvarodun.com

Requirements
Must have
• open mind
Nice to have
• open mind
Should not have
• DJ

```html
<!DOCTYPE html>
<html lang="en">
<head>
<meta charset="utf-8">
<title>Kelvaro – Business Card</title>
<link href="https://fonts.googleapis.com/css2?family=Roboto+Condensed:wght@400;700&display=swap" rel="stylesheet">
<style>
  :root {
    --bg: #e4e2de;
    --card-white: #ffffff;
    --ink: #1b1b1b;
    --band-dark: #2a2a2a;
    --band-mid: #4a4a4a;
    --band-light: #d8d8d8;
    --text-light: #f2f2f2;
    --back-black: #141414;
    --back-sheen: #2c2c2c;
  }
  * { margin: 0; padding: 0; box-sizing: border-box; }
  html, body { width: 1200px; height: 950px; overflow: hidden; }
  body {
    background: var(--bg);
    font-family: "Roboto Condensed", "Arial Narrow", sans-serif;
    position: relative;
  }
  .card {
    position: absolute;
    left: 230px;
    width: 740px;
    height: 423px;
    overflow: hidden;
    box-shadow: 0 10px 30px rgba(0,0,0,.25);
  }
  .card--front { top: 34px; background: var(--card-white); }
  .card--back {
    top: 492px;
    background: linear-gradient(110deg, var(--back-black) 0%, var(--back-black) 55%, var(--back-sheen) 75%, var(--back-black) 100%);
  }

  /* brand word */
  .brand {
    position: absolute;
    display: flex;
    align-items: center;
    gap: 16px;
    font-weight: 700;
    letter-spacing: 2px;
    line-height: 1;
  }
  .brand__square { width: 26px; height: 26px; }
  .card--front .brand { left: 52px; top: 170px; font-size: 78px; color: var(--ink); }
  .card--front .brand__square { background: var(--ink); }
  .card--back .brand { left: 0; right: 0; justify-content: center; top: 140px; font-size: 96px; color: var(--text-light); }
  .card--back .brand__square { background: var(--text-light); }

  .back-url {
    position: absolute;
    left: 0; right: 0;
    top: 268px;
    text-align: center;
    color: var(--text-light);
    font-size: 22px;
    letter-spacing: 4px;
  }

  /* contact bands */
  .contact-panel {
    position: absolute;
    top: 0; right: 0;
    width: 300px; height: 100%;
    display: flex;
    background: var(--band-light);
  }
  .band {
    position: relative;
    height: 100%;
    background: linear-gradient(180deg, var(--band-mid) 0%, var(--band-dark) 45%, var(--band-dark) 100%);
    color: var(--text-light);
  }
  .band--name { width: 104px; }
  .band--phone { width: 72px; margin-left: 22px; }
  .band--web { width: 72px; margin-left: 22px; }
  .band__text {
    position: absolute;
    bottom: 70px;
    left: 50%;
    writing-mode: vertical-rl;
    transform: translateX(-50%) rotate(180deg);
    white-space: nowrap;
    font-size: 24px;
    letter-spacing: 1px;
    line-height: 1.15;
  }
  .person-name { display: block; font-weight: 700; font-size: 26px; }
  .person-role { display: block; font-size: 21px; }
  .band__icon {
    position: absolute;
    bottom: 20px;
    left: 50%;
    width: 26px; height: 26px;
    transform: translateX(-50%);
    background: var(--text-light);
    border-radius: 3px;
  }
  .band__icon svg { width: 100%; height: 100%; display: block; }
</style>
</head>
<body>

<section class="card card--front" aria-label="Card front">
  <div class="brand"><span class="brand__square"></span><span class="brand__name">KELVARO</span></div>

  <div class="contact-panel">
    <div class="band band--name">
      <div class="band__text"><span class="person-name">MARCUS VALE</span><span class="person-role">PRESIDENT</span></div>
      <span class="band__icon"><svg viewBox="0 0 26 26"><circle cx="13" cy="10" r="4.5" fill="#2a2a2a"/><path d="M5 21c1-5 5-6 8-6s7 1 8 6z" fill="#2a2a2a"/></svg></span>
    </div>
    <div class="band band--phone">
      <div class="band__text">(318) 5024471963</div>
      <span class="band__icon"><svg viewBox="0 0 26 26"><path d="M8 5l3 0 1.5 4-2 1.5c1 2.2 2.8 4 5 5l1.5-2 4 1.5 0 3c0 1-1 2-2 2C11.5 20 6 14.5 6 7c0-1 1-2 2-2z" fill="#2a2a2a"/></svg></span>
    </div>
    <div class="band band--web">
      <div class="band__text">www.kelvarodun.com</div>
      <span class="band__icon"><svg viewBox="0 0 26 26"><circle cx="13" cy="13" r="8" fill="none" stroke="#2a2a2a" stroke-width="2"/><path d="M5 13h16M13 5c-3 3-3 13 0 16M13 5c3 3 3 13 0 16" fill="none" stroke="#2a2a2a" stroke-width="1.6"/></svg></span>
    </div>
  </div>
</section>

<section class="card card--back" aria-label="Card back">
  <div class="brand"><span class="brand__square"></span><span class="brand__name">KELVARO</span></div>
  <p class="back-url">KELVARODUN.COM</p>
</section>

</body>
</html>
```